Hello - we need a label design for our Quillon Health Hair Loss supplement. It is a natural hair loss supplement for black/african american women to regrow new hair and help restore hair loss & thinning hair due to vitamin deficiencies, traction alopecia, etc. It is a science based efficacious supplement with a centuries old medicinal herbal formula.
Attached is the logo & files of other generic competition and also Black hair products for your perusal. The label has to be a upscale and have an ethnic flair to it. The product is clinically effective, leveraged by Ancient Wisdom and Modern Science. The front of the label should include the following:
Quillon Health (logo)
Growth Accelerator
Advanced Women’s Hair Loss Formula
TRACTION ALOPECIA THERAPY
- Prevents hair loss & restores thinning, fragile hair
- Promotes Natural Hair Growth
- Strengthens Hair for less breakage
- Visibly increases hair density & thickness
- Thicker, Stronger, Longer, Hydrated hair
- Promotes Follicle regeneration & Hair Growth
Site-Specific for hair loss & stunted growth
60 capsules 30-day supply
Target Market(s)
Black/African American Women
Look and feel

```html
<!DOCTYPE html>
<html lang="en">
<head>
<meta charset="UTF-8">
<title>Quillon Health – Growth Accelerator Label</title>
<link href="https://fonts.googleapis.com/css2?family=Cinzel:wght@400;500&family=Roboto+Condensed:wght@300;400;700&display=swap" rel="stylesheet">
<style>
  :root {
    --page: #ffffff;
    --label-dark: #0c0907;
    --label-mid: #3a2316;
    --label-glow: #7a5238;
    --gold-light: #f3d39a;
    --gold: #d8a55e;
    --gold-deep: #a8733a;
    --ink-dark: #2a1b10;
    --text-white: #f6f2ec;
    --text-soft: #e2dcd4;
    --art-top: #4a3324;
    --art-bottom: #2a1d15;
  }
  * { margin: 0; padding: 0; box-sizing: border-box; }
  html, body {
    width: 1200px; height: 1200px; overflow: hidden;
    background: var(--page);
  }
  .label {
    position: absolute; left: 188px; top: 30px;
    width: 824px; height: 1140px; overflow: hidden;
    background:
      radial-gradient(ellipse 70% 55% at 80% 50%, var(--label-glow) 0%, var(--label-mid) 45%, rgba(20,12,8,0) 80%),
      linear-gradient(90deg, var(--label-dark) 0%, #1c120c 40%, #2c1c12 100%);
  }
  .brand-name {
    position: absolute; left: 117px; top: 205px;
    font-family: "Cinzel", serif; font-weight: 400;
    font-size: 54px; letter-spacing: 1px;
    color: var(--text-white);
  }
  .pill {
    position: absolute;
    background: linear-gradient(90deg, var(--gold-deep), var(--gold-light) 45%, var(--gold) 100%);
    color: var(--ink-dark);
    border-radius: 30px;
    display: flex; align-items: center; justify-content: center;
  }
  .pill--accelerator {
    left: 117px; top: 367px; width: 530px; height: 52px;
    font-family: "Cinzel", serif; font-size: 37px; font-weight: 500;
  }
  .headline {
    position: absolute; left: 117px; top: 462px;
    font-family: "Cinzel", serif; font-weight: 400;
    font-size: 64px; line-height: 61px; letter-spacing: -1px;
    color: var(--text-white);
  }
  .therapy-title {
    position: absolute; left: 120px; top: 682px;
    font-family: "Roboto Condensed", sans-serif; font-weight: 700;
    font-size: 22px; color: var(--text-white);
  }
  .benefits {
    position: absolute; left: 120px; top: 712px;
    list-style: none;
    font-family: "Roboto Condensed", sans-serif; font-weight: 300;
    font-size: 23px; line-height: 31px; color: var(--text-soft);
  }
  .benefits li::before { content: "• "; font-size: 15px; vertical-align: middle; }
  .gold-rule {
    position: absolute; left: 0; top: 900px; width: 824px; height: 40px;
  }
  .pill--small {
    left: 117px; height: 42px; padding: 0 10px;
    font-family: "Roboto Condensed", sans-serif; font-weight: 400;
    font-size: 27px; border-radius: 10px;
  }
  .pill--count { top: 984px; width: 170px; }
  .pill--supply { top: 1043px; width: 198px; }
  .seal {
    position: absolute; left: 378px; top: 978px;
    width: 112px; height: 112px; border-radius: 50%;
    border: 2px solid var(--text-white);
  }
  .follicle-art {
    position: absolute; left: 640px; top: 420px;
    width: 130px; height: 680px;
    border-radius: 8px;
    background: linear-gradient(180deg, var(--art-top) 0%, var(--art-bottom) 100%);
  }
</style>
</head>
<body>
  <div class="label">
    <div class="follicle-art" role="img" aria-label="Illustration of a single hair strand and follicle with golden sparkles"></div>

    <div class="brand-name">Quillon Health</div>

    <div class="pill pill--accelerator">GROWTH ACCELERATOR</div>

    <h1 class="headline">ADVANCED<br>WOMEN’S HAIR<br>LOSS FORMULA</h1>

    <div class="therapy-title">TRACTION ALOPECIA THERAPY</div>
    <ul class="benefits">
      <li>Prevents hair loss &amp; restores thinning, fragile hair</li>
      <li>Promotes Natural Hair Growth</li>
      <li>Strengthens Hair for less breakage</li>
      <li>Visibly increases hair density &amp; thickness</li>
      <li>Thicker, Stronger, Longer, Hydrated hair</li>
      <li>Promotes Follicle regeneration &amp; Hair Growth</li>
    </ul>

    <svg class="gold-rule" viewBox="0 0 824 40" aria-hidden="true">
      <path d="M90 22 Q330 6 620 20" fill="none" stroke="var(--gold)" stroke-width="2"/>
    </svg>

    <div class="pill pill--small pill--count">60 Capsules</div>
    <div class="pill pill--small pill--supply">30 Day Supply</div>

    <div class="seal" aria-hidden="true"></div>
  </div>
</body>
</html>
```